Landing page for Brook Aerowing

Re-design the landing page for www.brookaerowing.example. It needs to be flatter and work with both PC, Mac and Mobile. Sites I like are as follows:
http://tarnelflight.example
http://qoskyway.example
http://www.velmoplanes.example
http://www.dunmorewing.example/dmw.php
http://www.ulvane.example
http://www.cedrolskies.example
http://www.pembrookflighthub.example
http://www.corvallowings.example
http://www.tessorivawings.example

We are a Marlow 48 Dealer, SkyNoble FBO member, Vortell Circle FBO, QMR Preferred FBO located only 6 miles from Downtown Atlanta. Providing Aircraft charter, Aircraft sales, Aircraft Maintenance, Aircraft Line Services and Hangar, and Parts Support.

Reason: I have six people reviewing designs within the company and will not be able to complete the review until next week.

Target Market(s)

Pilot's looking for a place to take care of them in Atlanta

Industry/Entity Type

Group

Colors
fbed22
0555a3

Requirements
Must have
• Slogan "Focused on Arrival" and "Sensational Southern Service"

```html
<!DOCTYPE html>
<html lang="en">
<head>
<meta charset="utf-8">
<title>Brook Aerowing</title>
<link rel="stylesheet" href="https://fonts.googleapis.com/css2?family=Open+Sans:wght@400;600;700&display=swap">
<style>
:root{
  --blue:#0555a3;
  --yellow:#fbed22;
  --ink:#333;
  --grey-panel:#e1e1e1;
  --footer:#1f1f1f;
  --footer-base:#111;
}
*{box-sizing:border-box;margin:0;padding:0}
html,body{width:971px;height:1200px;overflow:hidden;background:#fff}
body{position:relative;font-family:"Open Sans",Arial,sans-serif;color:var(--ink)}
.abs{position:absolute}
.top-rule{left:0;top:0;width:971px;height:5px;background:var(--blue)}
.brand{left:138px;top:30px;display:flex;align-items:center;gap:10px}
.brand-mark{width:34px;height:34px;background:var(--yellow);border-radius:50%}
.brand-name{font-size:22px;font-weight:700;color:var(--blue)}
.contact{left:580px;top:34px;font-size:11px;color:#888;line-height:18px}
.contact-row{display:flex;align-items:center;gap:8px}
.contact svg{width:10px;height:10px;fill:#999}
.header-divider{left:708px;top:24px;width:1px;height:84px;background:#ddd}
.follow{left:731px;top:27px;font-size:10.5px;color:#888}
.social-top{left:731px;top:46px;display:flex;gap:7px}
.social-top span{width:20px;height:20px;display:block}
.nav{left:0;top:96px;width:971px;height:38px;background:var(--blue)}
.nav ul{position:absolute;left:138px;top:0;display:flex;list-style:none;height:38px}
.nav li{font-size:11.5px;color:#fff;padding:0 10px;line-height:38px;border-right:1px solid rgba(255,255,255,.12)}
.nav li.active{background:var(--yellow);color:var(--blue)}
.hero{left:0;top:134px;width:971px;height:298px;background:linear-gradient(180deg,#7f99b5 0%,#c8d5e2 55%,#aebdcd 100%)}
.hero h1{position:absolute;left:138px;top:56px;width:420px;font-size:26px;line-height:32px;font-weight:600;color:#333}
.hero p{position:absolute;left:138px;top:132px;font-size:11.5px;line-height:16px;color:#333}
.hero p b{color:var(--blue);font-weight:700}
.btn-more{left:138px;top:200px;width:122px;height:27px;background:var(--yellow);border:2px solid #c8a500;color:var(--blue);font-size:11.5px;font-weight:700;text-align:center;line-height:23px}
.hero-arrow{width:26px;height:26px;border-radius:50%;background:#fff;top:124px}
.hero-arrow svg{width:26px;height:26px}
.dots{left:431px;top:260px;display:flex;gap:6px}
.dots span{width:7px;height:7px;border-radius:50%;background:#fff;display:block}
.about{left:138px;top:455px;width:502px;font-size:11.2px;line-height:16.8px;color:#444}
.about-photo{float:left;width:114px;height:171px;margin:0 18px 4px 0;background:linear-gradient(180deg,#9aa2ab,#50565c)}
.about h2{font-size:22px;font-weight:600;color:var(--blue);line-height:26px;margin-bottom:4px}
.about a{color:var(--blue);font-weight:600;text-decoration:none}
.rule{left:138px;width:502px;height:1px;background:#ccc}
.services-title{left:138px;top:724px;width:502px;text-align:center;font-size:22px;font-weight:600;color:var(--blue)}
.services-sub{left:138px;top:760px;width:502px;text-align:center;font-size:12.5px;color:#444}
.tiles{left:138px;top:805px;display:flex;gap:10px}
.tile{width:93px;height:91px;background:var(--yellow);color:#333;font-weight:700;font-size:12.5px;display:flex;align-items:center;justify-content:center;text-align:center;line-height:16px;padding:4px}
.tile.active{background:var(--blue);color:var(--yellow)}
.promo{left:138px;top:961px;width:244px;height:97px;background:linear-gradient(180deg,#8aa0b6,#36465a);color:#fff;text-align:center}
.promo-big{font-size:22px;font-weight:700;margin-top:18px;line-height:24px}
.promo-small{font-size:12px;font-weight:700}
.promo-link{font-size:11px;color:var(--yellow)}
.partner{left:396px;top:961px;width:244px;height:97px;border:1px solid var(--blue);display:flex;align-items:center;justify-content:center;gap:8px;font-size:13px;font-weight:700;color:#333}
.partner i{width:16px;height:16px;background:#c0262e;border-radius:50%;display:block}
.clocks{left:653px;top:454px;width:179px;height:495px;background:var(--grey-panel);border:1px solid #c8c8c8}
.clock{position:absolute;left:22px;width:134px;height:68px;border:1px solid var(--blue)}
.clock .city{height:34px;background:var(--yellow);text-align:center;line-height:34px;font-size:12.5px;font-weight:700;color:var(--blue)}
.clock .time{height:32px;background:#f2f2f2;text-align:center;line-height:32px;font-size:14px;color:#444}
.footer{left:0;top:1098px;width:971px;height:64px;background:var(--footer)}
.footer h3{position:absolute;left:138px;top:17px;font-size:12px;font-weight:600;color:#fff}
.footer ul{position:absolute;left:138px;top:37px;display:flex;list-style:none;font-size:9px;color:#fff}
.footer li{padding-right:6px;margin-right:6px;border-right:1px solid #fff;line-height:10px}
.footer li:last-child{border:0}
.footer li.active{color:var(--blue)}
.base{left:0;top:1162px;width:971px;height:38px;background:var(--footer-base)}
.base p{position:absolute;left:138px;top:13px;font-size:8.5px;color:#ddd}
.social-bottom{position:absolute;left:634px;top:0;display:flex}
.social-bottom span{width:40px;height:38px;display:block;border-left:1px solid #2a2a2a;background:#1a1a1a}
.social-bottom span:first-child{background:#3a5a99}
</style>
</head>
<body>
<div class="abs top-rule"></div>

<header>
  <div class="abs brand"><span class="brand-mark"></span><span class="brand-name">Brook Aerowing</span></div>
  <div class="abs contact">
    <div class="contact-row"><svg viewBox="0 0 10 10"><path d="M2 0h2l1 3-1.5 1a6 6 0 0 0 2.5 2.5L7 5l3 1v2a2 2 0 0 1-2 2A8 8 0 0 1 0 2a2 2 0 0 1 2-2z"/></svg>555-014-2280</div>
    <div class="contact-row"><svg viewBox="0 0 10 10"><path d="M0 2h10v6H0z M0 2l5 3 5-3" stroke="#fff" stroke-width=".8"/></svg>info@brookaerowing.example</div>
  </div>
  <div class="abs header-divider"></div>
  <div class="abs follow">Follow us</div>
  <div class="abs social-top" aria-label="Social links">
    <span style="background:#3a5a99"></span><span style="background:#2aa3d8"></span><span style="background:#3d8cc6"></span><span style="background:#f07a24"></span>
  </div>
</header>

<nav class="abs nav">
  <ul>
    <li class="active">Home</li><li>About Us</li><li>Contact us</li><li>Resources</li><li>Aircraft sales</li><li>Parts</li><li>Maintenance</li><li>Fbo Services</li><li>Charter</li><li>Aircraft Management</li>
  </ul>
</nav>

<section class="abs hero" role="img" aria-label="Jet airliner flying above the clouds">
  <h1>Focused on Arrival and Sensational Southern Service</h1>
  <p>Let Brook Aerowing show you <b>Larkfield Avionics establishes Satellite Avionics</b><br>why we have been named <b>Location at Brook Aerowing KBRW</b><br>The #1 FBO in Georgia <b>Location in Atlantica, Georgia.</b></p>
  <div class="abs btn-more">Read more</div>
  <div class="abs hero-arrow" style="left:66px"><svg viewBox="0 0 26 26"><path d="M15 8l-5 5 5 5" fill="none" stroke="#999" stroke-width="1.5"/></svg></div>
  <div class="abs hero-arrow" style="left:864px"><svg viewBox="0 0 26 26"><path d="M11 8l5 5-5 5" fill="none" stroke="#999" stroke-width="1.5"/></svg></div>
  <div class="abs dots"><span></span><span></span><span></span><span></span><span></span><span></span></div>
</section>

<section class="abs about">
  <div class="about-photo" role="img" aria-label="Line technician marshalling a private jet"></div>
  <h2>About us</h2>
  <p>Atlanta's Most Established Fixed Based Operation established in 1955 by Southern Aviation Hall of Fame member Owen Brook, Sr. Our world class FBO facilities offer all the amenities for passengers and pilots, including computer work stations with internet access, plasma TV for catching up on national and world events, pilots lounge with theatre seating and security camera monitors and state of the art flight planning facilities. Our line technicians are FSTA Safety 1st trained and Brook Aerowing is a State of Georgia recognized drug-free workplace. Our concierge services can take care of passenger and crew ground transportation, hotel reservations and catering, we can even arrange for sporting event tickets or a round of golf. Let Brook Aerowing show you why we have been named the #1 FBO in Georgia multiple times. <a>Experience our "Sensational Southern Service"</a>.</p>
</section>

<div class="abs rule" style="top:708px"></div>
<h2 class="abs services-title">Aircraft Services</h2>
<p class="abs services-sub">Brook Aerowing offers a complete line of aircraft services including</p>
<div class="abs tiles">
  <div class="tile active">Aircraft Charter</div>
  <div class="tile">Block time</div>
  <div class="tile">Line Services</div>
  <div class="tile">Aircraft spares support</div>
  <div class="tile">Aircraft Sales</div>
</div>
<div class="abs rule" style="top:937px"></div>

<div class="abs promo" role="img" aria-label="Jet on the runway celebrating 50 years">
  <div class="promo-big">Celebrate 50 years</div>
  <div class="promo-small">of excellence</div>
  <div class="promo-link">Click here</div>
</div>
<div class="abs partner"><i></i>Marlow 48</div>

<aside class="abs clocks">
  <div class="clock" style="top:20px"><div class="city">ATLANTA</div><div class="time">03:50:01</div></div>
  <div class="clock" style="top:97px"><div class="city">GMT</div><div class="time">07:50:01</div></div>
  <div class="clock" style="top:174px"><div class="city">SAN FRANCISCO</div><div class="time">03:50:01</div></div>
  <div class="clock" style="top:251px"><div class="city">SALT LAKE</div><div class="time">01:50:01</div></div>
  <div class="clock" style="top:328px"><div class="city">DALLAS</div><div class="time">02:50:01</div></div>
  <div class="clock" style="top:405px"><div class="city">LONDON</div><div class="time">07:50:01</div></div>
</aside>

<footer class="abs footer">
  <h3>Quick links</h3>
  <ul>
    <li class="active">HOME</li><li>ABOUT US</li><li>CONTACT US</li><li>RESOURCES</li><li>AIRCRAFT SALES</li><li>PARTS</li><li>MAINTENANCE</li><li>FBO SERVICES</li><li>CHARTER</li><li>AIRCRAFT MANAGEMENT</li>
  </ul>
</footer>
<div class="abs base">
  <p>Copyright 2014. All right Reserved</p>
  <div class="social-bottom" aria-label="Social links"><span></span><span></span><span></span><span></span><span></span></div>
</div>
</body>
</html>
```